FotoVELTA buisnesscard

Hey :) I need a modern buisnesscard for my company FotoVELTA
It most have:
Dagligleder og Fotograf: Henrik Torvald Bjelland

Mob: +4791642058
Epost: post@fotovelta.no
Adresse: Bakkestien22, 6040 Fjordvik

Facbook and instagram logo with text FotoVELTA

FotoVELTA logo

It Company

```html
<!DOCTYPE html>
<html lang="no">
<head>
<meta charset="utf-8">
<title>FotoVELTA visittkort</title>
<link href="https://fonts.googleapis.com/css2?family=Inter:wght@400;500;800&display=swap" rel="stylesheet">
<style>
  :root {
    --bg: #0b0c0e;
    --purple: #4d0457;
    --purple-band: #5a0566;
    --purple-band-dark: #43034c;
    --blue: #05309c;
    --blue-shade: #022a8f;
    --ink: #ffffff;
    --ink-soft: rgba(255,255,255,0.85);
  }
  * { box-sizing: border-box; margin: 0; padding: 0; }
  html, body { width: 1200px; height: 850px; overflow: hidden; background: var(--bg); }
  body { font-family: "Inter", sans-serif; color: var(--ink); position: relative; }

  .card {
    position: absolute; top: 270px; width: 540px; height: 310px;
    overflow: hidden; box-shadow: 0 20px 40px rgba(0,0,0,0.6);
  }
  .card--front { left: 45px; background: var(--purple); }
  .card--back { left: 615px; background: var(--blue); }

  .card__bands { position: absolute; inset: 0; width: 100%; height: 100%; }

  .brand {
    display: flex; align-items: center; justify-content: center; gap: 8px;
    font-weight: 800; letter-spacing: 0.5px; color: var(--ink);
  }
  .brand__mark { background: var(--ink); }

  .card--front .brand { position: absolute; top: 52px; left: 0; right: 0; font-size: 22px; }
  .card--front .brand__mark { width: 12px; height: 12px; }

  .holder { position: absolute; top: 118px; left: 0; right: 0; text-align: center; }
  .holder__name { font-size: 26px; font-weight: 500; }
  .holder__role { font-size: 16px; font-weight: 400; margin-top: 6px; color: var(--ink-soft); }

  .contacts {
    position: absolute; bottom: 30px; left: 0; right: 0;
    display: flex; justify-content: center; gap: 26px;
    font-size: 12px; color: var(--ink-soft); white-space: nowrap;
  }
  .contacts__item { display: flex; align-items: center; gap: 6px; }
  .contacts__item svg { width: 11px; height: 11px; fill: var(--ink-soft); }

  .card--back .brand { position: absolute; top: 112px; left: 0; right: 0; font-size: 40px; }
  .card--back .brand__mark { width: 18px; height: 18px; }

  .socials {
    position: absolute; top: 218px; left: 0; right: 0;
    display: flex; justify-content: center; gap: 38px;
    font-size: 12px; color: var(--ink-soft);
  }
  .socials__item { display: flex; align-items: center; gap: 6px; }
  .socials__dot { width: 10px; height: 10px; border-radius: 50%; background: var(--ink-soft); }
</style>
</head>
<body>

<section class="card card--front">
  <svg class="card__bands" viewBox="0 0 540 310" preserveAspectRatio="none" aria-hidden="true">
    <polygon points="0,60 300,310 0,310" fill="var(--purple-band)"/>
    <polygon points="0,150 190,310 0,310" fill="var(--purple-band-dark)"/>
    <polygon points="0,90 260,260 250,268 0,102" fill="var(--purple-band-dark)"/>
  </svg>

  <div class="brand"><span class="brand__mark"></span>FotoVELTA</div>

  <div class="holder">
    <p class="holder__name">Henrik Torvald Bjelland</p>
    <p class="holder__role">Dagligleder og Fotograf</p>
  </div>

  <div class="contacts">
    <span class="contacts__item">
      <svg viewBox="0 0 24 24"><path d="M6.6 10.8a15 15 0 0 0 6.6 6.6l2.2-2.2c.3-.3.7-.4 1-.2 1.1.4 2.3.6 3.6.6.6 0 1 .4 1 1V20c0 .6-.4 1-1 1A17 17 0 0 1 3 4c0-.6.4-1 1-1h3.5c.6 0 1 .4 1 1 0 1.3.2 2.5.6 3.6.1.3 0 .7-.2 1z"/></svg>
      +4791642058
    </span>
    <span class="contacts__item">
      <svg viewBox="0 0 24 24"><path d="M2 5h20v14H2zm2 2v.3l8 6.2 8-6.2V7z"/></svg>
      post@fotovelta.no
    </span>
    <span class="contacts__item">
      <svg viewBox="0 0 24 24"><path d="M22 2 2 11l9 2 2 9z"/></svg>
      Bakkestien22, 6040 Fjordvik
    </span>
  </div>
</section>

<section class="card card--back">
  <svg class="card__bands" viewBox="0 0 540 310" preserveAspectRatio="none" aria-hidden="true">
    <polygon points="330,0 540,0 540,310 470,310" fill="var(--blue-shade)"/>
  </svg>

  <div class="brand"><span class="brand__mark"></span>FotoVELTA</div>

  <div class="socials">
    <span class="socials__item"><span class="socials__dot"></span>FotoVELTA</span>
    <span class="socials__item"><span class="socials__dot"></span>FotoVELTA</span>
  </div>
</section>

</body>
</html>
```